new KVR one page flyer

We need a 1 page A4 size flyer (need it asap please) that describes on 1 page with art work and using photos the services we provide. I have included some examples of old previous flyers from our other (seperate divisions of the business) I have named a photo called (photo for top of design) however you do your design this photo needs to be the star of the page by either having it at the top or bottom of the page please and we usually like this photo to be in greyscale colour.
we do like greyscale designs but are open to see what you come up with as a whole page of grey white and black might not suit.

Needs to list the following

Services include:
Over size loads / Hot Shot Loads
Heavy Vehicle Recovery services
Potable Water Deliveries
Road Building / Maintenance
Earthworks
Sand & Metal Supply & Cartage
Road Train Tippers
Road Train Tankers
Road Train Flat Tops
Drop Deck Trailers
Mine site accredited equipment & Operators.

We offer a large rage of services not listed so call us today for a personalised quote to suit your needs.

To go on the bottom of the page our contact details are

KVR Pty Ltd
Depot: Lot 514, Banksia Flats Track Coober Pedy
Mobile: 047 216 9381
email: darren@kestrelvaleroadworks.com.au

Target Market(s)

new clients

Colors

Designer to choose colors to be used in the design.

Requirements
Must have
• our services listed
Nice to have
• stand out designs

```html
<!DOCTYPE html>
<html lang="en">
<head>
<meta charset="utf-8">
<title>KVR Services Flyer</title>
<link href="https://fonts.googleapis.com/css2?family=Michroma&family=Montserrat:wght@400;500;700&display=swap" rel="stylesheet">
<style>
  :root {
    --page-bg: #a9a9a9;
    --paper: #ffffff;
    --charcoal: #2b2b2b;
    --charcoal-deep: #1f1f1f;
    --gold: #a57a3a;
    --gold-light: #c8994f;
    --steel: #6d6f73;
    --text-light: #f2f2f2;
    --sky-low: #c3c6c9;
    --earth: #9a5a36;
    --earth-dark: #6e3e24;
  }
  * { box-sizing: border-box; margin: 0; padding: 0; }
  html, body { width: 1200px; height: 1200px; overflow: hidden; }
  body {
    background: var(--page-bg);
    font-family: "Montserrat", Arial, sans-serif;
    display: flex; align-items: center; justify-content: center;
  }
  .flyer {
    position: relative;
    width: 780px; height: 1104px;
    background: var(--paper);
    overflow: hidden;
    box-shadow: 0 6px 18px rgba(0,0,0,.25);
  }
  .flyer__shapes { position: absolute; inset: 0; }
  .hero-title {
    position: absolute; left: 44px; top: 300px;
    font-family: "Michroma", "Arial Black", sans-serif;
    color: var(--paper);
    font-size: 38px; line-height: 1.15; letter-spacing: 2px;
    text-transform: uppercase;
  }
  .brand-name {
    position: absolute; right: 44px; top: 44px;
    font-family: "Michroma", "Arial Black", sans-serif;
    font-size: 50px; color: var(--charcoal);
  }
  .services {
    position: absolute; left: 56px; top: 575px; width: 396px;
    color: var(--text-light);
  }
  .services__title {
    font-size: 23px; font-weight: 700; letter-spacing: .5px; line-height: 28px;
    margin-bottom: 10px; text-transform: uppercase;
  }
  .services__title span { color: var(--gold-light); }
  .services__list { list-style: none; }
  .services__list li {
    position: relative; padding-left: 22px;
    font-size: 15.5px; line-height: 24px; font-weight: 500;
  }
  .services__list li::before {
    content: ""; position: absolute; left: 0; top: 9px;
    width: 7px; height: 7px; border-radius: 50%;
    background: var(--gold-light);
  }
  .services__note {
    margin-top: 14px; width: 392px;
    font-size: 14px; line-height: 21px; font-weight: 500;
  }
  .gallery {
    position: absolute; left: 478px; top: 350px; width: 282px;
    display: flex; flex-direction: column; gap: 22px;
  }
  .gallery__photo {
    height: 210px; border-radius: 16px;
    border: 4px solid var(--charcoal-deep);
  }
  .gallery__photo--road { background: linear-gradient(180deg, var(--sky-low) 0%, #8d8b86 55%, var(--earth) 100%); }
  .gallery__photo--tanker { background: linear-gradient(180deg, #5f7fc4 0%, #c9cfd8 50%, var(--earth) 100%); }
  .gallery__photo--grader { background: linear-gradient(180deg, #6f8ccc 0%, #d2c36a 55%, var(--earth-dark) 100%); }
  .contact {
    position: absolute; left: 50px; top: 964px; color: var(--paper);
  }
  .contact__company { font-size: 17px; font-weight: 700; line-height: 22px; margin-bottom: 4px; }
  .contact__row {
    display: flex; align-items: flex-start; gap: 12px;
    font-size: 14.5px; line-height: 20px; margin-top: 3px;
  }
  .contact__row svg { flex: none; margin-top: 2px; }
  .mascot {
    position: absolute; left: 382px; top: 968px;
    width: 78px; height: 78px; border-radius: 50%;
    background: radial-gradient(circle at 40% 35%, #8fd0ff, #2f7fd6 75%);
  }
  .website {
    position: absolute; right: 22px; bottom: 22px;
    color: var(--text-light); font-size: 15px; letter-spacing: .5px; font-weight: 500;
  }
</style>
</head>
<body>
<main class="flyer">
  <svg class="flyer__shapes" width="780" height="1104" viewBox="0 0 780 1104" aria-hidden="true">
    <defs>
      <linearGradient id="heroGradient" x1="0" y1="0" x2="0" y2="1">
        <stop offset="0" stop-color="#7c8592"/>
        <stop offset=".45" stop-color="#c4c7ca"/>
        <stop offset=".62" stop-color="#8a6a55"/>
        <stop offset="1" stop-color="#9a5a36"/>
      </linearGradient>
    </defs>
    <rect x="0" y="420" width="780" height="684" fill="#2b2b2b"/>
    <path d="M460 380 L780 300 L780 1040 L460 1040 Z" fill="#ffffff"/>
    <path d="M0 545 Q420 520 780 290 L780 318 Q430 548 0 565 Z" fill="#a57a3a"/>
    <path d="M0 545 Q420 520 780 290 L780 302 Q425 532 0 553 Z" fill="#6d6f73"/>
    <rect x="0" y="950" width="470" height="154" fill="#a57a3a"/>
    <rect x="470" y="1040" width="310" height="64" fill="#2b2b2b"/>
  </svg>

  <svg class="flyer__shapes" width="780" height="1104" viewBox="0 0 780 1104">
    <path role="img" aria-label="Road train tippers lined up on red outback dirt under a cloudy sky"
          d="M0 0 L780 0 L780 290 Q420 520 0 545 Z" fill="url(#heroGradient)"/>
  </svg>

  <div class="brand-name">KVR</div>
  <h1 class="hero-title">Kestrel Vale<br>Roadworks</h1>

  <section class="services">
    <h2 class="services__title"><span>Our</span> Services</h2>
    <ul class="services__list">
      <li>Over size loads / Hot Shot Loads</li>
      <li>Heavy Vehicle Recovery services</li>
      <li>Potable Water Deliveries</li>
      <li>Road Building / Maintenance</li>
      <li>Earthworks</li>
      <li>Sand &amp; Metal Supply &amp; Cartage</li>
      <li>Road Train Tippers</li>
      <li>Road Train Tankers</li>
      <li>Road Train Flat Tops</li>
      <li>Drop Deck Trailers</li>
      <li>Mine site accredited equipment &amp; Operators.</li>
    </ul>
    <p class="services__note">We offer a large range of services not listed so call us today for a personalised quote to suit your needs.</p>
  </section>

  <div class="gallery">
    <div class="gallery__photo gallery__photo--road" role="img" aria-label="Prime mover with trailers parked at the depot"></div>
    <div class="gallery__photo gallery__photo--tanker" role="img" aria-label="White water tanker truck on red dirt"></div>
    <div class="gallery__photo gallery__photo--grader" role="img" aria-label="Yellow road grader and loader on site"></div>
  </div>

  <div class="mascot" role="img" aria-label="Blue water drop mascot drinking from a bottle"></div>

  <section class="contact">
    <p class="contact__company">KVR Pty Ltd</p>
    <div class="contact__row">
      <svg width="16" height="16" viewBox="0 0 16 16" aria-hidden="true"><path d="M8 1 L15 8 H13 V15 H10 V10 H6 V15 H3 V8 H1 Z" fill="#fff"/></svg>
      <span>Lot 514, Banksia Flats Track<br>Coober Pedy</span>
    </div>
    <div class="contact__row">
      <svg width="16" height="16" viewBox="0 0 16 16" aria-hidden="true"><path d="M3 1 L6 1 L7 5 L5 6.5 Q6.5 9.5 9.5 11 L11 9 L15 10 L15 13 Q15 15 13 15 Q2 14 1 3 Q1 1 3 1 Z" fill="#fff"/></svg>
      <span>047 216 9381</span>
    </div>
    <div class="contact__row">
      <svg width="16" height="16" viewBox="0 0 16 16" aria-hidden="true"><rect x="1" y="3" width="14" height="10" fill="#fff"/><path d="M1 3 L8 9 L15 3" fill="none" stroke="#a57a3a" stroke-width="1.5"/></svg>
      <span>darren@kestrelvaleroadworks.com.au</span>
    </div>
  </section>

  <p class="website">www.kestrelvaleroadworks.com.au</p>
</main>
</body>
</html>
```